Professional law firm looking for new professional and eye-catching business card design

Law firm in need of new business card design using existing firm logo and firm colors on thick card stock. Firm colors are navy blue, cyan blue, and gray. Please use firm's logo either on the back of the card or on the front and back. I am looking for something eye-catching and resonating but also professional.

Target Market(s)

Law firm growth by attracting clients with professional, creative, and attractive business cards.

Industry/Entity Type

Legal/Law Firm

Contact Information for Business Card

Name: Derek T. Halloway, Esq., Address: 517 E. Quintley Blvd., P.O. Box 641, Tavares, FL 32790, Phone numbers: (352) 555-0187 Office, (352) 555-0142 Fax, email address: DerekH@hqlegalfx.com, website: www.HQLegalFX.com

Font styles to use
Other font styles liked:
• Font as close as possible to matching law firm logo.

Requirements
Must have
• Must have business card details and law firm logo with law firm colors.

```html
<!DOCTYPE html>
<html lang="en">
<head>
<meta charset="utf-8">
<title>HQ Legal – Business Card</title>
<link rel="stylesheet" href="https://fonts.googleapis.com/css2?family=Cinzel:wght@500;600&family=Libre+Baskerville&display=swap">
<style>
  :root {
    --backdrop: #efefef;
    --card: #3b3b3d;
    --card-deep: #333335;
    --cyan: #1ea7e6;
    --cream: #e8e6e1;
    --rule: #cfcfcf;
    --figure-light: #d9d9d9;
    --figure-shade: #8a8a8c;
    --ghost: #444446;
  }
  * { box-sizing: border-box; margin: 0; padding: 0; }
  html, body { width: 1200px; height: 800px; overflow: hidden; }
  body {
    background: var(--backdrop);
    display: flex;
    align-items: center;
    justify-content: center;
    gap: 40px;
  }
  .card {
    position: relative;
    width: 540px;
    height: 309px;
    border-radius: 22px;
    background: radial-gradient(circle at 40% 30%, var(--card) 0%, var(--card-deep) 100%);
    overflow: hidden;
    box-shadow: 0 10px 26px rgba(0,0,0,0.18);
  }

  /* Front */
  .front__ghost-art {
    position: absolute;
    left: 300px; top: 20px;
    width: 140px; height: 260px;
    border-radius: 70px 70px 20px 20px;
    background: linear-gradient(180deg, var(--ghost), var(--card-deep));
    opacity: 0.8;
  }
  .front__justice-art {
    position: absolute;
    right: 50px; top: 24px;
    width: 130px; height: 220px;
    border-radius: 40px 40px 14px 14px;
    background: linear-gradient(160deg, var(--figure-light) 0%, var(--figure-shade) 70%, var(--cyan) 100%);
  }
  .front__firm {
    position: absolute;
    left: 36px; bottom: 40px;
    color: var(--cyan);
    font-family: "Cinzel", serif;
    font-weight: 600;
  }
  .front__firm-name { font-size: 36px; letter-spacing: 3px; line-height: 1; white-space: nowrap; }
  .front__firm-rule { width: 210px; height: 1px; background: var(--rule); margin: 8px 0 6px; }
  .front__firm-entity { font-size: 13px; letter-spacing: 1px; white-space: nowrap; }

  /* Back */
  .back__logo {
    position: absolute;
    top: 26px; left: 50%;
    transform: translateX(-50%);
    display: flex;
    align-items: center;
    gap: 8px;
  }
  .back__logo-art {
    width: 26px; height: 72px;
    border-radius: 10px 10px 4px 4px;
    background: linear-gradient(170deg, var(--figure-light), var(--figure-shade) 75%, var(--cyan));
  }
  .back__logo-text {
    color: var(--cyan);
    font-family: "Cinzel", serif;
    font-weight: 600;
    white-space: nowrap;
  }
  .back__logo-name { font-size: 18px; letter-spacing: 2px; line-height: 1; }
  .back__logo-entity { font-size: 7px; letter-spacing: 0.5px; margin-top: 3px; }

  .back__name {
    position: absolute;
    top: 128px; left: 0; right: 0;
    text-align: center;
    color: var(--cyan);
    font-family: "Cinzel", serif;
    font-weight: 600;
    font-size: 22px;
    letter-spacing: 1.5px;
    white-space: nowrap;
  }
  .back__divider { position: absolute; top: 168px; left: 50px; width: 440px; height: 12px; }

  .back__address {
    position: absolute;
    left: 56px; top: 196px;
    color: var(--cream);
    font-family: "Libre Baskerville", serif;
    font-style: normal;
    font-size: 11.5px;
    line-height: 1.7;
    white-space: nowrap;
  }
  .back__contact {
    position: absolute;
    left: 300px; top: 192px;
    list-style: none;
    color: var(--cream);
    font-family: "Libre Baskerville", serif;
    font-size: 11.5px;
    white-space: nowrap;
  }
  .back__contact li { display: flex; align-items: center; gap: 9px; line-height: 1.75; }
  .back__contact svg { width: 11px; height: 11px; fill: var(--cyan); flex: none; }
</style>
</head>
<body>

<section class="card card--front" aria-label="Card front">
  <div class="front__ghost-art" role="img" aria-label="Faint large Lady Justice illustration in the background"></div>
  <div class="front__justice-art" role="img" aria-label="Lady Justice illustration in white with cyan scales and sword"></div>
  <div class="front__firm">
    <div class="front__firm-name">HQ LEGAL</div>
    <div class="front__firm-rule"></div>
    <div class="front__firm-entity">Halloway + Quint, P.A.</div>
  </div>
</section>

<section class="card card--back" aria-label="Card back">
  <div class="back__logo">
    <div class="back__logo-art" role="img" aria-label="Small Lady Justice illustration"></div>
    <div class="back__logo-text">
      <div class="back__logo-name">HQ LEGAL</div>
      <div class="back__logo-entity">Halloway + Quint, P.A.</div>
    </div>
  </div>

  <h1 class="back__name">DEREK T. HALLOWAY, ESQ.</h1>

  <svg class="back__divider" viewBox="0 0 440 12" aria-hidden="true">
    <line x1="0" y1="6" x2="226" y2="6" stroke="#cfcfcf" stroke-width="1.2"/>
    <rect x="230" y="2" width="8" height="8" fill="#e8e6e1" transform="rotate(45 234 6)"/>
    <line x1="242" y1="6" x2="440" y2="6" stroke="#cfcfcf" stroke-width="1.2"/>
  </svg>

  <address class="back__address">
    517 E. Quintley Blvd.,<br>
    P.O. Box 641, Larkmere, QV 00790
  </address>

  <ul class="back__contact">
    <li>
      <svg viewBox="0 0 24 24" aria-hidden="true"><path d="M6.6 10.8a15 15 0 0 0 6.6 6.6l2.2-2.2a1 1 0 0 1 1-.25 11.4 11.4 0 0 0 3.6.6 1 1 0 0 1 1 1V20a1 1 0 0 1-1 1A17 17 0 0 1 3 4a1 1 0 0 1 1-1h3.5a1 1 0 0 1 1 1c0 1.25.2 2.450.6 3.6a1 1 0 0 1-.25 1z"/></svg>
      (555) 555-0187
    </li>
    <li>
      <svg viewBox="0 0 24 24" aria-hidden="true"><circle cx="12" cy="12" r="10"/></svg>
      (555) 555-0142
    </li>
    <li>
      <svg viewBox="0 0 24 24" aria-hidden="true"><path d="M2 5h20v14H2z"/></svg>
      DerekH@hqlegalfx.com
    </li>
    <li>
      <svg viewBox="0 0 24 24" aria-hidden="true"><circle cx="12" cy="12" r="10"/></svg>
      www.HQLegalFX.com
    </li>
  </ul>
</section>

</body>
</html>
```